Double-sided business card needed - specific brief

We need a double sided business card designed for our company Radiant Trimline. Having lost a lot of weight myself, the back of the card needs to show my before and after pictures. It needs to cover the entire back side of the card. This might be with my two before pictures over set on top of my main after picture or in separate frames. I'll leave that to your artistic consideration. The front needs to have our logo with contact details centred below.

The cards will be printed by PRINTKO.com and will be rectangular, 84mm x 55mm, but with ROUNDED edges. Please therefore present your designs rectangular but with rounded edges if possible.

The card should be designed in LANDSCAPE orientation.

As well as the logo, the front of the card should have the following details:

Moira Blakewell
Weight Loss Motivator with 189lb personal loss
moira@radiant-trimline.example
+44 (0)7700 900418

The website is important so should perhaps be more bold than the rest:
www.radiant-trimline.example

My brand colours are: Pink #CD2366, Light Pink #FD88AD. Blue #1C9CB1, Light Blue #64C4DE

Target Market(s)

Women 30+

Contact Information for Business Card

As description above

Font styles to use
Sans Serif

Requirements
Must have
• Double sided.
• Back side entirely covered with my before and after pictures.
• You may wish to float my before pictures on top of my after picture or add them in different frames. I look forward to seeing your different suggestions.

```html
<!DOCTYPE html>
<html lang="en">
<head>
<meta charset="utf-8">
<title>Radiant Trimline – Business Card</title>
<link rel="stylesheet" href="https://fonts.googleapis.com/css2?family=Cinzel:wght@400;700&family=Montserrat:wght@300;400;500&display=swap">
<style>
  :root {
    --pink: #CD2366;
    --light-pink: #FD88AD;
    --blue: #1C9CB1;
    --light-blue: #64C4DE;
    --ink: #1d1d1f;
    --grey-text: #4a4a4a;
    --icon-yellow: #f0c419;
    --circle-blue: #2b3a9a;
    --card-white: #ffffff;
    --backdrop: #e9e7e4;
  }
  * { box-sizing: border-box; margin: 0; padding: 0; }
  html, body { width: 1200px; height: 892px; overflow: hidden; }
  body {
    background: var(--backdrop);
    position: relative;
    font-family: "Montserrat", sans-serif;
  }
  .card {
    position: absolute;
    top: 269px;
    width: 540px;
    height: 354px;
    background: var(--card-white);
    border-radius: 22px;
    overflow: hidden;
    box-shadow: 0 6px 20px rgba(0,0,0,.15);
  }
  .card--front { left: 40px; }
  .card--back  { left: 620px; }

  /* Front */
  .brand {
    position: absolute;
    top: 44px;
    left: 0; right: 0;
    display: flex;
    align-items: center;
    justify-content: center;
    gap: 12px;
  }
  .brand__dot {
    width: 40px; height: 40px;
    border-radius: 50%;
    background: var(--light-blue);
  }
  .brand__name {
    font-family: "Cinzel", serif;
    font-weight: 400;
    font-size: 34px;
    color: var(--pink);
    letter-spacing: 1px;
  }
  .holder {
    position: absolute;
    top: 128px;
    left: 70px;
    font-family: "Cinzel", serif;
    font-weight: 700;
    font-size: 24px;
    color: var(--ink);
  }
  .contacts {
    position: absolute;
    top: 170px;
    left: 70px;
    list-style: none;
    font-size: 13px;
    color: var(--grey-text);
    line-height: 22px;
  }
  .contacts li { display: flex; align-items: center; gap: 8px; }
  .contacts__icon {
    width: 14px; height: 14px;
    border-radius: 50%;
    background: var(--icon-yellow);
    flex: none;
  }
  .contacts__web { padding-left: 22px; font-weight: 500; color: var(--ink); }
  .swoosh { position: absolute; left: 0; bottom: 0; }

  /* Back */
  .photo {
    position: absolute;
    top: 0;
    height: 176px;
  }
  .photo--before {
    left: 20px; width: 250px;
    background: linear-gradient(135deg, #e9e2dc, #d8b8a2 55%, #8a3a2e);
  }
  .photo--after {
    left: 270px; width: 250px;
    background: linear-gradient(135deg, #6a5a48, #c9b8a0 50%, #3b2f2a);
  }
  .badge {
    position: absolute;
    left: 190px; top: 160px;
    width: 160px; height: 120px;
    border-radius: 50%;
    background: var(--circle-blue);
    display: flex; align-items: center; justify-content: center;
  }
  .badge__photo {
    width: 92px; height: 94px;
    background: linear-gradient(180deg, #b9c7d8, #7e9a6a 60%, #4f7a3a);
  }
  .label {
    position: absolute;
    display: flex; flex-direction: column; align-items: center;
    font-family: "Cinzel", serif;
    font-weight: 700;
    font-size: 22px;
    color: var(--ink);
  }
  .label svg { margin-bottom: 14px; }
  .label--before { left: 76px; top: 202px; }
  .label--before svg { margin-bottom: 10px; }
  .label--after { left: 392px; top: 232px; }
</style>
</head>
<body>

<section class="card card--front" aria-label="Card front">
  <div class="brand">
    <span class="brand__dot"></span>
    <span class="brand__name">Radiant Trimline</span>
  </div>
  <h1 class="holder">Moira Blakewell</h1>
  <ul class="contacts">
    <li><span class="contacts__icon"></span>Weight Loss Motivator with 189lb personal loss</li>
    <li><span class="contacts__icon"></span>+44 (0)7700 900418</li>
    <li><span class="contacts__icon"></span>moira@radiant-trimline.example</li>
    <li class="contacts__web">www.radiant-trimline.example</li>
  </ul>
  <svg class="swoosh" width="540" height="354" viewBox="0 0 540 354" aria-hidden="true">
    <path d="M0 354 L0 330 C150 320 330 300 540 190 L540 354 Z" fill="var(--ink)"/>
  </svg>
</section>

<section class="card card--back" aria-label="Card back">
  <div class="photo photo--before" role="img" aria-label="Before photo: owner in wedding veil"></div>
  <div class="photo photo--after" role="img" aria-label="After photo: owner seated on a leather sofa"></div>
  <div class="badge">
    <div class="badge__photo" role="img" aria-label="Photo of owner outdoors holding a small dog"></div>
  </div>
  <div class="label label--before">
    <svg width="16" height="26" viewBox="0 0 16 26" aria-hidden="true"><path d="M8 0 L16 12 H10 V26 H6 V12 H0 Z" fill="var(--ink)"/></svg>
    <span>Before</span>
  </div>
  <div class="label label--after">
    <svg width="16" height="26" viewBox="0 0 16 26" aria-hidden="true"><path d="M8 0 L16 12 H10 V26 H6 V12 H0 Z" fill="var(--ink)"/></svg>
    <span>After</span>
  </div>
</section>

</body>
</html>
```